Tovrimel Complete Stationery - Logo already designed

I already have the logo designed see attached. I need have a full set of stationary and business card designed for printing. I have attached an example of what I mean.

Please feel free to be creative. Also you can use the X in the logo by its self if you think it will work.

My details:

Name: Dorian Pelsett
Social media handles: @dorianpelsett
W: dorianpelsett.com
E: info@dorianpelsett.com
​P: 08 7349 5286
PO Box 3872, Wendlemore 6047
ABN 83 274 908 615

Target Market(s)

Anyone looking to be inspired.

Industry/Entity Type

Business

Font styles to use
Sans Serif

Colors
fbee3e
000000

Requirements
Must have
• My details:
• Name: Dorian Pelsett
• Social media handles: @dorianpelsett
• W: dorianpelsett.com
• E: info@dorianpelsett.com
• ​P: 08 7349 5286
• PO Box 3872, Wendlemore 6047
• ABN 83 274 908 615
Nice to have
• Something a little different
Should not have
• must not look tacky.

```html
<!DOCTYPE html>
<html lang="en">
<head>
<meta charset="utf-8">
<title>Tovrimel – Business Card</title>
<link rel="stylesheet" href="https://fonts.googleapis.com/css2?family=Oswald:wght@500;700&family=Didact+Gothic&display=swap">
<style>
  :root {
    --card-bg: #2f3538;
    --accent: #f7c600;
    --ink: #111213;
    --light: #ffffff;
    --page: #ffffff;
  }
  html, body {
    margin: 0;
    padding: 0;
    width: 1200px;
    height: 1200px;
    overflow: hidden;
    background: var(--page);
  }
  .canvas {
    position: relative;
    width: 1200px;
    height: 1200px;
  }
  .card-back {
    position: absolute;
    left: 24px;
    top: 389px;
    width: 534px;
    height: 386px;
    background: var(--card-bg);
    color: var(--light);
    font-family: "Didact Gothic", sans-serif;
  }
  .holder-name {
    position: absolute;
    left: 23px;
    top: 26px;
    margin: 0;
    font-family: "Oswald", sans-serif;
    font-weight: 500;
    font-size: 31px;
    line-height: 1;
    letter-spacing: 7px;
    color: var(--accent);
  }
  .handle {
    position: absolute;
    left: 23px;
    top: 80px;
    margin: 0;
    font-size: 27px;
    line-height: 1;
  }
  .contact-row {
    position: absolute;
    left: 23px;
    display: flex;
    align-items: flex-start;
  }
  .contact-icon {
    width: 42px;
    height: 42px;
    flex: none;
  }
  .contact-text {
    margin-left: 43px;
    font-size: 24px;
    line-height: 29px;
    padding-top: 6px;
    white-space: nowrap;
  }
  .row-web { top: 139px; }
  .row-mail { top: 192px; }
  .row-phone { top: 247px; }
  .row-post { top: 300px; }
  .row-post .contact-text { padding-top: 8px; }

  .brand-front {
    position: absolute;
    left: 694px;
    top: 527px;
    width: 344px;
    height: 102px;
    display: flex;
    align-items: center;
    justify-content: center;
    gap: 14px;
  }
  .brand-mark {
    width: 26px;
    height: 26px;
    background: var(--accent);
  }
  .brand-name {
    font-family: "Oswald", sans-serif;
    font-weight: 700;
    font-size: 74px;
    line-height: 1;
    color: var(--ink);
    letter-spacing: 1px;
  }
</style>
</head>
<body>
<main class="canvas">
  <section class="card-back">
    <h1 class="holder-name">Dorian Pelsett</h1>
    <p class="handle">@dorianpelsett</p>

    <div class="contact-row row-web">
      <svg class="contact-icon" viewBox="0 0 42 42" aria-hidden="true">
        <circle cx="21" cy="21" r="19.5" fill="var(--accent)"/>
        <circle cx="21" cy="21" r="17" fill="var(--ink)"/>
        <text x="21" y="25" text-anchor="middle" font-family="Didact Gothic, sans-serif" font-size="11" fill="var(--accent)">www</text>
      </svg>
      <span class="contact-text">dorianpelsett.com</span>
    </div>

    <div class="contact-row row-mail">
      <svg class="contact-icon" viewBox="0 0 42 42" aria-hidden="true">
        <circle cx="21" cy="21" r="19.5" fill="var(--accent)"/>
        <circle cx="21" cy="21" r="17" fill="var(--ink)"/>
        <rect x="10" y="13.5" width="22" height="15" fill="none" stroke="var(--accent)" stroke-width="1.4"/>
        <path d="M10 13.5 L21 23 L32 13.5 M10 28.5 L18 21 M32 28.5 L24 21" fill="none" stroke="var(--accent)" stroke-width="1.4"/>
      </svg>
      <span class="contact-text">info@dorianpelsett.com</span>
    </div>

    <div class="contact-row row-phone">
      <svg class="contact-icon" viewBox="0 0 42 42" aria-hidden="true">
        <circle cx="21" cy="21" r="19.5" fill="var(--accent)"/>
        <circle cx="21" cy="21" r="17" fill="var(--ink)"/>
        <path d="M14 11 l4 -1 l3 6 l-3 2 c1 3 3 6 6 8 l2 -3 l6 3 l-1 4 c-1 1 -3 2 -5 1 c-7 -3 -12 -9 -14 -15 c0 -2 1 -4 2 -5 z" fill="var(--accent)"/>
      </svg>
      <span class="contact-text">08 7349 5286</span>
    </div>

    <div class="contact-row row-post">
      <svg class="contact-icon" viewBox="0 0 42 42" aria-hidden="true">
        <circle cx="21" cy="21" r="19.5" fill="var(--accent)"/>
        <circle cx="21" cy="21" r="17" fill="var(--ink)"/>
        <path d="M21 34 C16 26 13 22 13 17 a8 8 0 0 1 16 0 C29 22 26 26 21 34 z" fill="var(--accent)"/>
        <circle cx="21" cy="17" r="3.5" fill="var(--ink)"/>
      </svg>
      <span class="contact-text">PO Box 3872, Wendlemore 6047<br>ABN 83 274 908 615</span>
    </div>
  </section>

  <section class="brand-front">
    <span class="brand-mark"></span>
    <span class="brand-name">TOVRIMEL</span>
  </section>
</main>
</body>
</html>
```